Bref créative
Business Card for "Homeward by Plan"
Business card for senior move management company
Simple
Dalia Fenwick
Owner / CEO
Lindenbrook, IL
dalia@homeplanex.com
www.homeplanex.com
Relocation | Organizing | Interior Design
Attached is the file for the homeward by plan business cards
png logo file for homewrd by plan
jpeg for homeward by plan business cards

```html
<!DOCTYPE html>
<html lang="en">
<head>
<meta charset="utf-8">
<title>Homeward by Plan — Business Card</title>
<link href="https://fonts.googleapis.com/css2?family=Tinos:wght@400;700&display=swap" rel="stylesheet">
<style>
  :root {
    --page: #ffffff;
    --green: #5d7a1e;
    --green-light: #86a13a;
    --green-dark: #4a6315;
    --brown: #8d725c;
    --ink: #111111;
    --white: #ffffff;
    --edge: #3a3a3a;
  }
  html, body {
    margin: 0;
    padding: 0;
    width: 1200px;
    height: 1055px;
    overflow: hidden;
    background: var(--page);
    font-family: "Tinos", "Times New Roman", serif;
  }
  .canvas { position: relative; width: 1200px; height: 1055px; }

  .card {
    position: absolute;
    box-sizing: border-box;
    border: 2px solid var(--edge);
    overflow: hidden;
  }

  /* Front */
  .card--front { left: 28px; top: 34px; width: 824px; height: 474px; background: var(--white); }
  .brand {
    position: absolute;
    display: flex;
    align-items: center;
    gap: 26px;
  }
  .brand__dot { border-radius: 50%; flex: none; }
  .brand__name {
    font-weight: 700;
    line-height: 1.05;
    letter-spacing: 0.5px;
    text-transform: uppercase;
  }
  .card--front .brand { left: 196px; top: 56px; }
  .card--front .brand__dot { width: 112px; height: 112px; background: var(--green); }
  .card--front .brand__name { color: var(--brown); font-size: 38px; }

  .name-band {
    position: absolute;
    left: 0; right: 0; top: 237px; height: 76px;
    background: var(--green);
    color: var(--white);
    text-align: center;
  }
  .name-band__name { font-size: 34px; line-height: 1; margin-top: 8px; }
  .name-band__title { font-size: 20px; margin-top: 6px; }

  .contact {
    position: absolute;
    left: 0; right: 0; top: 324px;
    text-align: center;
    color: var(--ink);
    font-size: 21px;
    line-height: 29px;
  }

  /* Back */
  .card--back {
    left: 310px; top: 550px; width: 835px; height: 465px;
    background: radial-gradient(ellipse at 50% 45%, var(--green-light) 0%, var(--green) 45%, var(--green-dark) 100%);
  }
  .card--back .brand { left: 172px; top: 168px; }
  .card--back .brand__dot { width: 100px; height: 100px; background: var(--white); opacity: 0.9; }
  .card--back .brand__name { color: var(--white); font-size: 38px; }

  .services {
    position: absolute;
    left: 0; right: 0; top: 410px;
    text-align: center;
    color: var(--white);
    font-size: 21px;
    letter-spacing: 0.3px;
  }
</style>
</head>
<body>
<main class="canvas">
  <section class="card card--front" aria-label="Business card front">
    <div class="brand">
      <span class="brand__dot" aria-hidden="true"></span>
      <div class="brand__name">Homeward<br>by Plan</div>
    </div>
    <div class="name-band">
      <div class="name-band__name">Dalia Fenwick</div>
      <div class="name-band__title">Owner / CEO</div>
    </div>
    <div class="contact">
      <div>Lindenbrook, IL</div>
      <div>Phone: 847.555.0142</div>
      <div>Email: dalia@homeplanex.com</div>
      <div>www.homeplanex.com</div>
    </div>
  </section>

  <section class="card card--back" aria-label="Business card back">
    <div class="brand">
      <span class="brand__dot" aria-hidden="true"></span>
      <div class="brand__name">Homeward<br>by Plan</div>
    </div>
    <div class="services">Relocation | Organizing | Interior Design</div>
  </section>
</main>
</body>
</html>
```